Health and Wellbeing online Shop

I have attached a specification, however in summary this is a new business startup selling vitamins and supplements.

We need a web design for new wellbeing website, selling high end vitamins, supplements and nootropics. Therefore I need a simple eCommerce solution .

I need the website to look very different to other websites on the market. The more creative the better. It should look fresh elegant and simple. The criteria for products being on my site is that they have great reviews and they have been scientifically tested.

You will need the option of being able to log into an account, either through pagebook, snoople, chirpnet, Pixogram or create an account with email. For accounts, users will need the facility to reset passwords, see previous orders, track current order, and maintain favourites.

It should be PC, mobile and tablet friendly.

Look and Feel

It should be an elegant, modern, professional, trendy, unisex website. It should look clean and calm. Am happy to try interesting and slightly unusual designs. I would also like to have chat functionality, either powered by volKAtalk or by Bax 61.

Websites I like are
https://www.corvan-radiance.co.uk/
https://www.plainnutrients.co.uk/
http://www.lumadermis.com/

PLEASE DO USE YOUR KNOWELDGE OF WHAT WORKS FOR WEB DESIGN. YOU’RE THE EXPERT AND NEED YOUR EXPERTISE. CARTE BLANCHE TO DESIGN AS YOU SEE FIT. Please be creative, I need my site to stand out from the crowd.

Target Market(s)
Middle aged women are our most common client, however, younger patients, both male and female, will often visit the site. In summary, I would like the site to appeal to all age brackets.

Industry/Entity Type
Business

Coding
Coded - Design and coding required

Number of Pages Required
5 pages
Updates

I would like more designs. I was expecting 75+ Designs to choose from as per the package I paid for.

Target Market(s)

Industry/Entity Type

Health And Wellness

Coding

Number of Pages Required

5+ page

Requirements
Must have
• Creative design

```html
<!DOCTYPE html>
<html lang="en">
<head>
<meta charset="utf-8">
<title>Solvia – Vitamins &amp; Nootropics Shop</title>
<link href="https://fonts.googleapis.com/css2?family=Baskervville:wght@400;700&display=swap" rel="stylesheet">
<style>
:root{
  --ink:#1a1a1a;
  --muted:#5e5e5e;
  --line:#9a9a9a;
  --rule:#666;
  --foot:#878787;
  --paper:#fff;
  --stage:#fff;
}
*{box-sizing:border-box;margin:0;padding:0}
html,body{width:1200px;height:1200px;overflow:hidden;background:var(--stage)}
body{font-family:'Baskervville',serif;color:var(--ink);position:relative}
.stage{position:absolute;left:0;top:0;width:1932px;height:1932px;transform:scale(.62112);transform-origin:0 0}
.screen{position:absolute;background:var(--paper);overflow:hidden;box-shadow:0 12px 26px rgba(0,0,0,.38)}
.abs{position:absolute}

/* header */
.hdr{position:absolute;left:0;top:0;width:100%;height:52px;border-bottom:1px solid var(--rule)}
.brand{position:absolute;left:7.3%;top:16px;display:flex;align-items:baseline;gap:10px;font-size:9px;letter-spacing:.5px}
.brand b{font-weight:400;font-size:17px;letter-spacing:.5px}
.search{position:absolute;left:45.4%;top:21px;display:flex;gap:8px;align-items:center;font-size:9.5px}
.search i{display:block;width:182px;height:16px;border:1px solid #777;border-radius:8px}
.hlink{position:absolute;top:22px;font-size:9.5px}
.hlink.login{left:76%}
.hlink.signup{left:81.6%}
.cart{position:absolute;left:89%;top:20px;display:flex;align-items:center;gap:2px}
.cart em{font-style:normal;background:#000;color:#fff;font-size:7px;border-radius:6px;padding:0 6px;line-height:10px}
.nav{position:absolute;left:0;top:52px;width:100%;height:25px;border-bottom:1px solid var(--rule);display:flex;justify-content:center;align-items:center;gap:46px;font-size:7.5px;letter-spacing:.4px}

/* sidebar */
.side{position:absolute;width:92px}
.side h4{font-weight:400;font-size:10.5px;display:flex;justify-content:space-between;align-items:center;border-bottom:1px solid var(--line);height:16px}
.side ul{list-style:none}
.side li{font-size:8.8px;color:var(--muted);height:15.6px;line-height:14px;border-bottom:1px solid #bbb;white-space:nowrap}
.side.tight li{height:15px;line-height:13.5px}

/* product cards */
.row{position:absolute;display:grid;grid-template-columns:repeat(4,147px);justify-items:center}
.grid{position:absolute;display:grid;grid-template-columns:repeat(4,141.5px);row-gap:16px}
.card{width:100px;text-align:center}
.card.boxed{width:101px;height:166px;border:1px solid #444;padding-top:6px}
.jar{width:40px;height:80px;margin:0 auto;border-radius:7px 7px 4px 4px;background:linear-gradient(#3b2c26 0 16%,#c65a2a 16% 24%,#ea7038 24% 88%,#b9532b 88%)}
.pn{font-size:7.6px;line-height:7.4px;margin-top:10px}
.stars{font-size:10px;letter-spacing:1px;margin-top:6px}
.pr{font-size:8px;margin-top:3px;color:#333}
.add{display:inline-block;background:#000;color:#fff;font-size:5.8px;padding:2px 14px;border-radius:5px;margin-top:5px;font-weight:700}
.sec-title{position:absolute;font-size:15px;border-bottom:1px solid #333;line-height:17px}
.more{position:absolute;text-align:center;font-size:8.5px;border-bottom:1px solid #555;padding-bottom:3px}

.pill{display:inline-block;background:#000;color:#fff;border-radius:10px;text-align:center}
.msg{position:absolute;background:#000;color:#fff;font-size:7px;border-radius:10px 0 0 10px;display:flex;align-items:center;justify-content:center}

/* footer */
.foot{position:absolute;left:0;width:100%;background:var(--foot);color:#fff}
.foot .col{position:absolute;top:14px}
.foot h5{font-weight:400;font-size:9px;text-decoration:underline;margin-bottom:6px}
.foot p{font-size:6.2px;line-height:9.5px}
.c1{left:7.3%}.c2{left:33%}.c3{left:58.8%}.c4{left:84.4%}

/* home */
.hero{left:58px;top:78px;width:666px;height:218px;background:#f4f4f5}
.hero-photo{position:absolute;inset:0;clip-path:polygon(0 0,550px 0,330px 100%,0 100%);background:linear-gradient(160deg,#e9e9ec,#c9c9ce 70%,#b9b3c2)}
.hero-text{position:absolute;right:0;top:60px;text-align:right;font-size:21.5px;line-height:23px}
.hero .pill{position:absolute;right:0;top:184px;width:93px;height:15px;font-size:8.5px;line-height:15px}
.about-photo{left:180px;top:817px;width:544px;height:201px;background:linear-gradient(120deg,#dedee2,#cfd0d6 50%,#e2e1e5)}
.about{left:180px;top:826px;width:544px;text-align:center}
.about h3{font-weight:400;font-size:15px;display:inline-block;border-bottom:1px solid #333;line-height:17px}
.about p{font-size:8.6px;line-height:12.6px;width:510px;margin:12px auto 0}
.about .pill{font-size:5.8px;font-weight:700;width:68px;height:10px;line-height:10px;margin-top:14px}
.contact{left:180px;top:1036px;width:544px;text-align:center;font-size:8.5px;line-height:12.6px}
.contact h3{font-weight:400;font-size:15px;display:inline-block;border-bottom:1px solid #333;line-height:17px;margin-bottom:14px}

/* shop */
.banner{left:0;top:77px;width:100%;height:90px;background:linear-gradient(90deg,#f4ece0 0%,#ecc27c 30%,#e6a84a 48%,#f0d29c 70%,#f5ede2 100%)}
.banner.pale{background:linear-gradient(90deg,#f7f2ea,#f1d7a8 45%,#f6ede0)}
.banner-text{left:0;top:88px;width:100%;text-align:center}
.banner-text h2{font-weight:400;font-size:26px;display:inline-block;border-bottom:1.5px solid #222;line-height:26px}
.banner-text p{font-size:7.2px;line-height:11px;width:630px;margin:8px auto 0}
.filter{left:171px;top:184px;width:524px;border-bottom:1px solid #555;font-size:8.5px;height:14px}
.filter span{position:absolute;top:0}
.filter u{text-decoration:underline}

/* product detail */
.ptitle{position:absolute;left:57px;top:86px;font-size:13px}
.hr{position:absolute;left:0;width:100%;border-top:1px solid var(--rule)}
.vr{position:absolute;top:108px;height:198px;border-left:1px solid var(--rule)}
.spec{left:57px;top:128px;font-size:8px}
.spec b{display:block;font-weight:400;font-size:13.5px;line-height:13px;margin:4px 0 10px}
.bigjar{left:360px;top:146px;width:62px;height:117px;border-radius:10px 10px 6px 6px;background:linear-gradient(#3b2c26 0 15%,#c65a2a 15% 22%,#ea7038 22% 90%,#b9532b 90%)}
.buy{right:57px;top:166px;text-align:right;width:260px}
.buy h2{font-weight:400;font-size:15px;line-height:13.5px}
.buy .big-stars{font-size:14px;letter-spacing:1.5px;margin-top:16px}
.buy .line{display:flex;justify-content:flex-end;gap:24px;font-size:10px;margin-top:4px;align-items:baseline}
.buy .line strong{font-weight:400;font-size:13.5px}
.buy .pill{width:104px;height:18px;line-height:18px;font-size:11px;margin-top:6px;border-radius:9px}
.desc-h{left:57px;top:313px;font-size:13px;border-bottom:1px solid #333;line-height:15px}
.dcol{position:absolute;top:338px;font-size:6.9px;line-height:11.3px;color:#444}
.dcol p{margin-bottom:7px}

/* cart */
.cart-title{left:53px;top:80px;font-size:13px}
table.items{position:absolute;left:53px;top:123px;width:382px;border-collapse:collapse}
.items td,.items th{border:1px solid #999;height:28px;font-size:9.5px;padding:0 6px;font-weight:400}
.items th{height:30px;color:#666;font-size:9px}
.items td.x{text-align:center;width:29px}
.items td.q{text-align:center;width:27px;font-size:8px}
.items td.p{font-size:12px;width:57px}
table.totals{position:absolute;left:560px;top:123px;width:135px;border-collapse:collapse}
.totals td,.totals th{border:1px solid #999;height:29px;font-size:8.5px;font-weight:400;text-align:center}
.totals th{font-size:11.5px}
.totals td.v{font-size:11.5px}
.cbtn{position:absolute;top:294px;width:102px;height:20px;line-height:20px;font-size:8.5px;border-radius:10px}

/* auth */
.auth{left:1555px;top:650px;width:377px;height:960px;background:linear-gradient(180deg,#f4f4f4,#fafafa 40%,#f3f3f3);box-shadow:none}
.box{position:absolute;background:#fff;border:1px solid #ccc}
.box .t{position:absolute;left:14px}
.box .welcome{font-size:14px}
.box .head{font-size:16px}
.box .lbl{font-size:11px;color:#555}
.box .inp{position:absolute;height:22px;border:1px solid #999;border-radius:5px}
.box .small{font-size:8.5px;color:#555}
.box .pill{position:absolute;font-size:11px;height:19px;line-height:19px;border-radius:6px}
.social{position:absolute;left:0;top:265px;width:100%;display:flex;justify-content:space-around;padding:0 6px}
.social span{display:flex;flex-direction:column;align-items:center;gap:2px;font-size:6px}
.social i{display:block;width:16px;height:16px;border-radius:50%;background:#111}
</style>
</head>
<body>
<div class="stage">

<!-- ===== Home ===== -->
<section class="screen" style="left:0;top:0;width:782px;height:1265px">
  <header class="hdr">
    <div class="brand"><b>Solvia</b><span>RESTORE &nbsp;|&nbsp; RENEW &nbsp;|&nbsp; THRIVE</span></div>
    <div class="search"><span>Search</span><i></i></div>
    <span class="hlink login">Log In</span><span class="hlink signup">Sign Up</span>
    <span class="cart"><svg width="18" height="14" viewBox="0 0 18 14"><path d="M0 1h3l2 8h9l2-6H4" fill="none" stroke="#111" stroke-width="1.3"/><circle cx="6.5" cy="12" r="1.3"/><circle cx="12.5" cy="12" r="1.3"/></svg><em>0</em></span>
  </header>
  <nav class="nav"><span>VITAMINS</span><span>NOOTROPICS</span><span>ABOUT US</span><span>CONTACT US</span></nav>

  <div class="abs hero">
    <div class="hero-photo" role="img" aria-label="Photo of a woman stretching on a yoga mat"></div>
    <div class="hero-text">Welcome to<br>your favorite one-stop<br>Shop for all your<br>Vitamin &amp; Nootropics<br>Needs</div>
    <span class="pill">Enter Shop</span>
  </div>

  <aside class="side" style="left:58px;top:318px">
    <h4>Our Categories <svg width="10" height="10" viewBox="0 0 10 10"><circle cx="5" cy="5" r="4.3" fill="none" stroke="#333" stroke-width=".8"/><path d="M3 6l2-2 2 2" fill="none" stroke="#333" stroke-width=".8"/></svg></h4>
    <ul style="margin-bottom:30px">
      <li>Amino Acids</li><li>Antioxidants</li><li>Cannabis Oil CBD</li><li>Chondroitin</li><li>Coenzyme Q10</li><li>Cod Liver Oil</li><li>Essential Fatty Acids</li><li>Evening Primrose Oils</li><li>Fish Oils</li><li>Glucosamine</li><li>Herbal / Botanical</li><li>Minerals</li><li>MultiVitamins</li><li>Omega-3</li><li>Pregnancy</li><li>Probiotics</li><li>Vegan</li><li>Vegeterian</li><li>Vitamin B</li><li>Vitamin C</li><li>Vitamin D</li><li>Vitamin E</li><li>Vitamin K</li>
    </ul>
    <h4>Interest <svg width="10" height="10" viewBox="0 0 10 10"><circle cx="5" cy="5" r="4.3" fill="none" stroke="#333" stroke-width=".8"/><path d="M3 6l2-2 2 2" fill="none" stroke="#333" stroke-width=".8"/></svg></h4>
    <ul style="margin-bottom:14px">
      <li>Ageing</li><li>Bone Health</li><li>Children's Health</li><li>Circulation</li><li>Digestive Health</li><li>Energy</li><li>Eye Health</li><li>Heart Health</li><li>Immune System</li><li>Joints &amp; Muscles</li><li>Memory</li><li>Menopause</li><li>Men's Health</li><li>Skin / Hair / Beauty</li><li>Sleep / Relax</li><li>Slimming</li><li>Sports</li><li>Stress / Mood</li><li>Women's Health</li>
    </ul>
    <h4>Delivery <svg width="10" height="10" viewBox="0 0 10 10"><circle cx="5" cy="5" r="4.3" fill="none" stroke="#333" stroke-width=".8"/><path d="M3 6l2-2 2 2" fill="none" stroke="#333" stroke-width=".8"/></svg></h4>
    <ul><li>Tablet</li><li>Liposomal</li><li>Suppository</li><li>Intravenous</li><li>Spray</li><li>Pump</li><li>Nebulised</li></ul>
  </aside>

  <h3 class="sec-title" style="left:180px;top:320px;font-weight:400">Vitamins</h3>
  <div class="row" style="left:157px;top:360px">
    <div class="card"><div class="jar" role="img" aria-label="Orange supplement jar"></div><p class="pn">Flexa-Core™ Care<br>1500mg Glucosamine<br>x 180 tablets</p><p class="stars">★★★★★</p><p class="pr">from $11.89</p><span class="add">Add to Cart</span></div>
    <div class="card"><div class="jar" role="img" aria-label="Orange supplement jar"></div><p class="pn">Flexa-Core™ Care<br>1500mg Glucosamine<br>x 180 tablets</p><p class="stars">★★★★★</p><p class="pr">from $11.89</p><span class="add">Add to Cart</span></div>
    <div class="card"><div class="jar" role="img" aria-label="Orange supplement jar"></div><p class="pn">Flexa-Core™ Care<br>1500mg Glucosamine<br>x 180 tablets</p><p class="stars">★★★★★</p><p class="pr">from $11.89</p><span class="add">Add to Cart</span></div>
    <div class="card"><div class="jar" role="img" aria-label="Orange supplement jar"></div><p class="pn">Flexa-Core™ Care<br>1500mg Glucosamine<br>x 180 tablets</p><p class="stars">★★★★★</p><p class="pr">from $11.89</p><span class="add">Add to Cart</span></div>
  </div>
  <div class="more" style="left:180px;top:536px;width:544px">See More</div>

  <h3 class="sec-title" style="left:180px;top:568px;font-weight:400">Nootropics</h3>
  <div class="row" style="left:157px;top:608px">
    <div class="card"><div class="jar" role="img" aria-label="Orange supplement jar"></div><p class="pn">Flexa-Core™ Care<br>1500mg Glucosamine<br>x 180 tablets</p><p class="stars">★★★★★</p><p class="pr">from $11.89</p><span class="add">Add to Cart</span></div>
    <div class="card"><div class="jar" role="img" aria-label="Orange supplement jar"></div><p class="pn">Flexa-Core™ Care<br>1500mg Glucosamine<br>x 180 tablets</p><p class="stars">★★★★★</p><p class="pr">from $11.89</p><span class="add">Add to Cart</span></div>
    <div class="card"><div class="jar" role="img" aria-label="Orange supplement jar"></div><p class="pn">Flexa-Core™ Care<br>1500mg Glucosamine<br>x 180 tablets</p><p class="stars">★★★★★</p><p class="pr">from $11.89</p><span class="add">Add to Cart</span></div>
    <div class="card"><div class="jar" role="img" aria-label="Orange supplement jar"></div><p class="pn">Flexa-Core™ Care<br>1500mg Glucosamine<br>x 180 tablets</p><p class="stars">★★★★★</p><p class="pr">from $11.89</p><span class="add">Add to Cart</span></div>
  </div>
  <div class="more" style="left:180px;top:784px;width:544px">See More</div>

  <div class="abs about-photo" role="img" aria-label="Soft faded photo of a group yoga class"></div>
  <div class="abs about">
    <h3>About Us</h3>
    <p>Lorem ipsum dolor sit amet, consectetur adipiscing elit. Phasellus non sodales ipsum. Pellentesque ac nisi eu sem suscipit luctus. Duis commodo aliquam mi, non pellentesque est finibus vitae. Maecenas ut faucibus magna, eget volutpat lorem. Nunc vestibulum ut nunc ut tincidunt. Curabitur non ante porttitor lectus volutpat imperdiet interdum sit amet erat. Maecenas convallis erat massa, sit amet faucibus purus imperdiet sed. Sed tellus odio, ullamcorper sed elit consequat, pretium dictum dui.<br>Morbi a euismod sapien, ac porttitor sem. Suspendisse molestie at urna quis accumsan. Suspendisse potenti. Integer id dui elementum, feugiat erat quis, ultricies dolor. Quisque in ullamcorper purus, efficitur ultrices leo. Nullam non gravida nunc, eget interdum mi. Suspendisse ac nisi aliquet, tempus urna vitae, venenatis nibh. Vestibulum aliquet in tellus et aliquet. Praesent consequat arcu et mauris porttitor, ut lacinia dui lobortis. Praesent hendrerit dolor eu lacinia venenatis. Mauris porta auctor ex lacinia mollis. Morbi euismod massa a lacinia porttitor</p>
    <span class="pill">Learn More</span>
  </div>

  <div class="abs contact">
    <h3>Contact Us</h3>
    <p>Get in touch for expert confidential supplement advice, or for customer services.</p>
    <p style="margin-top:12px;font-weight:700">Calling from the UK</p>
    <p>+44 20 7946 0321</p>
    <p>To contact us by email, please click the send us a message tab on the right.</p>
    <p>Our team is available</p>
    <p>Monday - Friday: 08:00 - 18:00</p>
    <p>Answer phone out of hours</p>
  </div>
  <div class="msg" style="left:683px;top:1153px;width:99px;height:19px">Send us a message</div>

  <footer class="foot" style="top:1183px;height:82px">
    <div class="col c1"><h5>Help &amp; Information</h5><p>About Us<br>Careers at Brindle<br>Corporate Responsibility<br>Investors Site</p></div>
    <div class="col c2"><h5>About Solvia</h5><p>About Us<br>Careers at Brindle<br>Corporate Responsibility<br>Investors Site</p></div>
    <div class="col c3"><h5>More From Solvia</h5><p>About Us<br>Careers at Brindle<br>Corporate Responsibility<br>Investors Site</p></div>
    <div class="col c4"><h5>Our &nbsp;Partners</h5><p>About Us<br>Careers at Brindle<br>Corporate Responsibility<br>Investors Site</p></div>
  </footer>
</section>

<!-- ===== Shop: Nootropics ===== -->
<section class="screen" style="left:802px;top:0;width:750px;height:1265px">
  <header class="hdr">
    <div class="brand"><b>Solvia</b><span>RESTORE &nbsp;|&nbsp; RENEW &nbsp;|&nbsp; THRIVE</span></div>
    <div class="search"><span>Search</span><i></i></div>
    <span class="hlink login">Log In</span><span class="hlink signup">Sign Up</span>
    <span class="cart"><svg width="18" height="14" viewBox="0 0 18 14"><path d="M0 1h3l2 8h9l2-6H4" fill="none" stroke="#111" stroke-width="1.3"/><circle cx="6.5" cy="12" r="1.3"/><circle cx="12.5" cy="12" r="1.3"/></svg><em>0</em></span>
  </header>
  <nav class="nav"><span>VITAMINS</span><span>NOOTROPICS</span><span>ABOUT US</span><span>CONTACT US</span></nav>
  <div class="abs banner" role="img" aria-label="Close-up photo of golden supplement capsules"></div>
  <div class="abs banner-text">
    <h2>Our Products</h2>
    <p>Lorem ipsum dolor sit amet, consectetur adipiscing elit. Phasellus non sodales ipsum. Pellentesque ac nisi eu sem suscipit luctus. Duis commodo aliquam mi, non pellentesque est finibus vitae. Maecenas ut faucibus magna, eget volutpat lorem. Nunc vestibulum ut nunc ut tincidunt. Curabitur non ante porttitor lectus volutpat imperdiet interdum sit amet erat. Maecenas convallis erat massa, sit amet faucibus purus imperdiet sed. Sed tellus odio, ullamcorper sed elit consequat, pretium dictum dui.</p>
  </div>

  <aside class="side tight" style="left:54px;top:184px;width:88px">
    <h4>Our Categories <svg width="10" height="10" viewBox="0 0 10 10"><circle cx="5" cy="5" r="4.3" fill="none" stroke="#333" stroke-width=".8"/><path d="M3 6l2-2 2 2" fill="none" stroke="#333" stroke-width=".8"/></svg></h4>
    <ul style="margin-bottom:22px">
      <li>Amino Acids</li><li>Antioxidants</li><li>Cannabis Oil CBD</li><li>Chondroitin</li><li>Coenzyme Q10</li><li>Cod Liver Oil</li><li>Essential Fatty Acids</li><li>Evening Primrose Oils</li><li>Fish Oils</li><li>Glucosamine</li><li>Herbal / Botanical</li><li>Minerals</li><li>MultiVitamins</li><li>Omega-3</li><li>Pregnancy</li><li>Probiotics</li><li>Vegan</li><li>Vegeterian</li><li>Vitamin B</li><li>Vitamin C</li><li>Vitamin D</li><li>Vitamin E</li><li>Vitamin K</li>
    </ul>
    <h4>Interest <svg width="10" height="10" viewBox="0 0 10 10"><circle cx="5" cy="5" r="4.3" fill="none" stroke="#333" stroke-width=".8"/><path d="M3 6l2-2 2 2" fill="none" stroke="#333" stroke-width=".8"/></svg></h4>
    <ul style="margin-bottom:14px">
      <li>Ageing</li><li>Bone Health</li><li>Children's Health</li><li>Circulation</li><li>Digestive Health</li><li>Energy</li><li>Eye Health</li><li>Heart Health</li><li>Immune System</li><li>Joints &amp; Muscles</li><li>Memory</li><li>Menopause</li><li>Men's Health</li><li>Skin / Hair / Beauty</li><li>Sleep / Relax</li><li>Slimming</li><li>Sports</li><li>Stress / Mood</li><li>Women's Health</li>
    </ul>
    <h4>Delivery <svg width="10" height="10" viewBox="0 0 10 10"><circle cx="5" cy="5" r="4.3" fill="none" stroke="#333" stroke-width=".8"/><path d="M3 6l2-2 2 2" fill="none" stroke="#333" stroke-width=".8"/></svg></h4>
    <ul><li>Tablet</li><li>Liposomal</li><li>Suppository</li><li>Intravenous</li><li>Spray</li><li>Pump</li><li>Nebulised</li></ul>
  </aside>

  <div class="abs filter"><span style="left:0;color:#666">Filter Results:</span><span style="left:62px"><u>Name</u> ⌄</span><span style="left:131px"><u>Top Sellers</u> ⌄</span><span style="left:220px"><u>Review Score</u> ⌄</span><span style="left:319px"><u>Price</u> ⌄</span></div>
  <h3 class="abs" style="left:171px;top:211px;font-size:15px;font-weight:400">Nootropics</h3>
  <div class="grid" style="left:171px;top:246px">
    <div class="card boxed"><div class="jar" role="img" aria-label="Orange supplement jar"></div><p class="pn">Flexa-Core™ Care<br>1500mg Glucosamine<br>x 180 tablets</p><p class="stars">★★★★★</p><p class="pr">from $11.89</p><span class="add">Add to Cart</span></div>
    <div class="card boxed"><div class="jar" role="img" aria-label="Orange supplement jar"></div><p class="pn">Flexa-Core™ Care<br>1500mg Glucosamine<br>x 180 tablets</p><p class="stars">★★★★★</p><p class="pr">from $11.89</p><span class="add">Add to Cart</span></div>
    <div class="card boxed"><div class="jar" role="img" aria-label="Orange supplement jar"></div><p class="pn">Flexa-Core™ Care<br>1500mg Glucosamine<br>x 180 tablets</p><p class="stars">★★★★★</p><p class="pr">from $11.89</p><span class="add">Add to Cart</span></div>
    <div class="card boxed"><div class="jar" role="img" aria-label="Orange supplement jar"></div><p class="pn">Flexa-Core™ Care<br>1500mg Glucosamine<br>x 180 tablets</p><p class="stars">★★★★★</p><p class="pr">from $11.89</p><span class="add">Add to Cart</span></div>
    <div class="card boxed"><div class="jar" role="img" aria-label="Orange supplement jar"></div><p class="pn">Flexa-Core™ Care<br>1500mg Glucosamine<br>x 180 tablets</p><p class="stars">★★★★★</p><p class="pr">from $11.89</p><span class="add">Add to Cart</span></div>
    <div class="card boxed"><div class="jar" role="img" aria-label="Orange supplement jar"></div><p class="pn">Flexa-Core™ Care<br>1500mg Glucosamine<br>x 180 tablets</p><p class="stars">★★★★★</p><p class="pr">from $11.89</p><span class="add">Add to Cart</span></div>
    <div class="card boxed"><div class="jar" role="img" aria-label="Orange supplement jar"></div><p class="pn">Flexa-Core™ Care<br>1500mg Glucosamine<br>x 180 tablets</p><p class="stars">★★★★★</p><p class="pr">from $11.89</p><span class="add">Add to Cart</span></div>
    <div class="card boxed"><div class="jar" role="img" aria-label="Orange supplement jar"></div><p class="pn">Flexa-Core™ Care<br>1500mg Glucosamine<br>x 180 tablets</p><p class="stars">★★★★★</p><p class="pr">from $11.89</p><span class="add">Add to Cart</span></div>
    <div class="card boxed"><div class="jar" role="img" aria-label="Orange supplement jar"></div><p class="pn">Flexa-Core™ Care<br>1500mg Glucosamine<br>x 180 tablets</p><p class="stars">★★★★★</p><p class="pr">from $11.89</p><span class="add">Add to Cart</span></div>
    <div class="card boxed"><div class="jar" role="img" aria-label="Orange supplement jar"></div><p class="pn">Flexa-Core™ Care<br>1500mg Glucosamine<br>x 180 tablets</p><p class="stars">★★★★★</p><p class="pr">from $11.89</p><span class="add">Add to Cart</span></div>
    <div class="card boxed"><div class="jar" role="img" aria-label="Orange supplement jar"></div><p class="pn">Flexa-Core™ Care<br>1500mg Glucosamine<br>x 180 tablets</p><p class="stars">★★★★★</p><p class="pr">from $11.89</p><span class="add">Add to Cart</span></div>
    <div class="card boxed"><div class="jar" role="img" aria-label="Orange supplement jar"></div><p class="pn">Flexa-Core™ Care<br>1500mg Glucosamine<br>x 180 tablets</p><p class="stars">★★★★★</p><p class="pr">from $11.89</p><span class="add">Add to Cart</span></div>
    <div class="card boxed"><div class="jar" role="img" aria-label="Orange supplement jar"></div><p class="pn">Flexa-Core™ Care<br>1500mg Glucosamine<br>x 180 tablets</p><p class="stars">★★★★★</p><p class="pr">from $11.89</p><span class="add">Add to Cart</span></div>
    <div class="card boxed"><div class="jar" role="img" aria-label="Orange supplement jar"></div><p class="pn">Flexa-Core™ Care<br>1500mg Glucosamine<br>x 180 tablets</p><p class="stars">★★★★★</p><p class="pr">from $11.89</p><span class="add">Add to Cart</span></div>
    <div class="card boxed"><div class="jar" role="img" aria-label="Orange supplement jar"></div><p class="pn">Flexa-Core™ Care<br>1500mg Glucosamine<br>x 180 tablets</p><p class="stars">★★★★★</p><p class="pr">from $11.89</p><span class="add">Add to Cart</span></div>
    <div class="card boxed"><div class="jar" role="img" aria-label="Orange supplement jar"></div><p class="pn">Flexa-Core™ Care<br>1500mg Glucosamine<br>x 180 tablets</p><p class="stars">★★★★★</p><p class="pr">from $11.89</p><span class="add">Add to Cart</span></div>
    <div class="card boxed"><div class="jar" role="img" aria-label="Orange supplement jar"></div><p class="pn">Flexa-Core™ Care<br>1500mg Glucosamine<br>x 180 tablets</p><p class="stars">★★★★★</p><p class="pr">from $11.89</p><span class="add">Add to Cart</span></div>
    <div class="card boxed"><div class="jar" role="img" aria-label="Orange supplement jar"></div><p class="pn">Flexa-Core™ Care<br>1500mg Glucosamine<br>x 180 tablets</p><p class="stars">★★★★★</p><p class="pr">from $11.89</p><span class="add">Add to Cart</span></div>
    <div class="card boxed"><div class="jar" role="img" aria-label="Orange supplement jar"></div><p class="pn">Flexa-Core™ Care<br>1500mg Glucosamine<br>x 180 tablets</p><p class="stars">★★★★★</p><p class="pr">from $11.89</p><span class="add">Add to Cart</span></div>
    <div class="card boxed"><div class="jar" role="img" aria-label="Orange supplement jar"></div><p class="pn">Flexa-Core™ Care<br>1500mg Glucosamine<br>x 180 tablets</p><p class="stars">★★★★★</p><p class="pr">from $11.89</p><span class="add">Add to Cart</span></div>
  </div>
  <div class="more" style="left:171px;top:1156px;width:524px">See More</div>
  <div class="msg" style="left:656px;top:1157px;width:94px;height:18px">Send us a message</div>
  <footer class="foot" style="top:1185px;height:80px">
    <div class="col c1"><h5>Help &amp; Information</h5><p>About Us<br>Careers at Brindle<br>Corporate Responsibility<br>Investors Site</p></div>
    <div class="col c2"><h5>About Solvia</h5><p>About Us<br>Careers at Brindle<br>Corporate Responsibility<br>Investors Site</p></div>
    <div class="col c3"><h5>More From Solvia</h5><p>About Us<br>Careers at Brindle<br>Corporate Responsibility<br>Investors Site</p></div>
    <div class="col c4"><h5>Our &nbsp;Partners</h5><p>About Us<br>Careers at Brindle<br>Corporate Responsibility<br>Investors Site</p></div>
  </footer>
</section>

<!-- ===== Shop: Vitamins (small) ===== -->
<section class="screen" style="left:1555px;top:0;width:750px;height:1265px;transform:scale(.5027);transform-origin:0 0">
  <header class="hdr">
    <div class="brand"><b>Solvia</b><span>RESTORE &nbsp;|&nbsp; RENEW &nbsp;|&nbsp; THRIVE</span></div>
    <div class="search"><span>Search</span><i></i></div>
    <span class="hlink login">Log In</span><span class="hlink signup">Sign Up</span>
    <span class="cart"><svg width="18" height="14" viewBox="0 0 18 14"><path d="M0 1h3l2 8h9l2-6H4" fill="none" stroke="#111" stroke-width="1.3"/><circle cx="6.5" cy="12" r="1.3"/><circle cx="12.5" cy="12" r="1.3"/></svg><em>0</em></span>
  </header>
  <nav class="nav"><span>VITAMINS</span><span>NOOTROPICS</span><span>ABOUT US</span><span>CONTACT US</span></nav>
  <div class="abs banner pale" role="img" aria-label="Soft photo of golden supplement capsules"></div>
  <div class="abs banner-text">
    <h2>Our Products</h2>
    <p>Lorem ipsum dolor sit amet, consectetur adipiscing elit. Phasellus non sodales ipsum. Pellentesque ac nisi eu sem suscipit luctus. Duis commodo aliquam mi, non pellentesque est finibus vitae. Maecenas ut faucibus magna, eget volutpat lorem. Nunc vestibulum ut nunc ut tincidunt. Curabitur non ante porttitor lectus volutpat imperdiet interdum sit amet erat. Maecenas convallis erat massa, sit amet faucibus purus imperdiet sed.</p>
  </div>
  <aside class="side tight" style="left:54px;top:184px;width:88px">
    <h4>Our Categories <svg width="10" height="10" viewBox="0 0 10 10"><circle cx="5" cy="5" r="4.3" fill="none" stroke="#333" stroke-width=".8"/><path d="M3 6l2-2 2 2" fill="none" stroke="#333" stroke-width=".8"/></svg></h4>
    <ul style="margin-bottom:22px">
      <li>Amino Acids</li><li>Antioxidants</li><li>Cannabis Oil CBD</li><li>Chondroitin</li><li>Coenzyme Q10</li><li>Cod Liver Oil</li><li>Essential Fatty Acids</li><li>Evening Primrose Oils</li><li>Fish Oils</li><li>Glucosamine</li><li>Herbal / Botanical</li><li>Minerals</li><li>MultiVitamins</li><li>Omega-3</li><li>Pregnancy</li><li>Probiotics</li><li>Vegan</li><li>Vegeterian</li><li>Vitamin B</li><li>Vitamin C</li><li>Vitamin D</li><li>Vitamin E</li><li>Vitamin K</li>
    </ul>
    <h4>Interest <svg width="10" height="10" viewBox="0 0 10 10"><circle cx="5" cy="5" r="4.3" fill="none" stroke="#333" stroke-width=".8"/><path d="M3 6l2-2 2 2" fill="none" stroke="#333" stroke-width=".8"/></svg></h4>
    <ul style="margin-bottom:14px">
      <li>Ageing</li><li>Bone Health</li><li>Children's Health</li><li>Circulation</li><li>Digestive Health</li><li>Energy</li><li>Eye Health</li><li>Heart Health</li><li>Immune System</li><li>Joints &amp; Muscles</li><li>Memory</li><li>Menopause</li><li>Men's Health</li><li>Skin / Hair / Beauty</li><li>Sleep / Relax</li><li>Slimming</li><li>Sports</li><li>Stress / Mood</li><li>Women's Health</li>
    </ul>
    <h4>Delivery <svg width="10" height="10" viewBox="0 0 10 10"><circle cx="5" cy="5" r="4.3" fill="none" stroke="#333" stroke-width=".8"/><path d="M3 6l2-2 2 2" fill="none" stroke="#333" stroke-width=".8"/></svg></h4>
    <ul><li>Tablet</li><li>Liposomal</li><li>Suppository</li><li>Intravenous</li><li>Spray</li><li>Pump</li><li>Nebulised</li></ul>
  </aside>
  <div class="abs filter"><span style="left:0;color:#666">Filter Results:</span><span style="left:62px"><u>Name</u> ⌄</span><span style="left:131px"><u>Top Sellers</u> ⌄</span><span style="left:220px"><u>Review Score</u> ⌄</span><span style="left:319px"><u>Price</u> ⌄</span></div>
  <h3 class="abs" style="left:171px;top:211px;font-size:15px;font-weight:400">Vitamins</h3>
  <div class="grid" style="left:171px;top:246px">
    <div class="card boxed"><div class="jar" role="img" aria-label="Orange supplement jar"></div><p class="pn">Flexa-Core™ Care<br>1500mg Glucosamine<br>x 180 tablets</p><p class="stars">★★★★★</p><p class="pr">from $11.89</p><span class="add">Add to Cart</span></div>
    <div class="card boxed"><div class="jar" role="img" aria-label="Orange supplement jar"></div><p class="pn">Flexa-Core™ Care<br>1500mg Glucosamine<br>x 180 tablets</p><p class="stars">★★★★★</p><p class="pr">from $11.89</p><span class="add">Add to Cart</span></div>
    <div class="card boxed"><div class="jar" role="img" aria-label="Orange supplement jar"></div><p class="pn">Flexa-Core™ Care<br>1500mg Glucosamine<br>x 180 tablets</p><p class="stars">★★★★★</p><p class="pr">from $11.89</p><span class="add">Add to Cart</span></div>
    <div class="card boxed"><div class="jar" role="img" aria-label="Orange supplement jar"></div><p class="pn">Flexa-Core™ Care<br>1500mg Glucosamine<br>x 180 tablets</p><p class="stars">★★★★★</p><p class="pr">from $11.89</p><span class="add">Add to Cart</span></div>
    <div class="card boxed"><div class="jar" role="img" aria-label="Orange supplement jar"></div><p class="pn">Flexa-Core™ Care<br>1500mg Glucosamine<br>x 180 tablets</p><p class="stars">★★★★★</p><p class="pr">from $11.89</p><span class="add">Add to Cart</span></div>
    <div class="card boxed"><div class="jar" role="img" aria-label="Orange supplement jar"></div><p class="pn">Flexa-Core™ Care<br>1500mg Glucosamine<br>x 180 tablets</p><p class="stars">★★★★★</p><p class="pr">from $11.89</p><span class="add">Add to Cart</span></div>
    <div class="card boxed"><div class="jar" role="img" aria-label="Orange supplement jar"></div><p class="pn">Flexa-Core™ Care<br>1500mg Glucosamine<br>x 180 tablets</p><p class="stars">★★★★★</p><p class="pr">from $11.89</p><span class="add">Add to Cart</span></div>
    <div class="card boxed"><div class="jar" role="img" aria-label="Orange supplement jar"></div><p class="pn">Flexa-Core™ Care<br>1500mg Glucosamine<br>x 180 tablets</p><p class="stars">★★★★★</p><p class="pr">from $11.89</p><span class="add">Add to Cart</span></div>
    <div class="card boxed"><div class="jar" role="img" aria-label="Orange supplement jar"></div><p class="pn">Flexa-Core™ Care<br>1500mg Glucosamine<br>x 180 tablets</p><p class="stars">★★★★★</p><p class="pr">from $11.89</p><span class="add">Add to Cart</span></div>
    <div class="card boxed"><div class="jar" role="img" aria-label="Orange supplement jar"></div><p class="pn">Flexa-Core™ Care<br>1500mg Glucosamine<br>x 180 tablets</p><p class="stars">★★★★★</p><p class="pr">from $11.89</p><span class="add">Add to Cart</span></div>
    <div class="card boxed"><div class="jar" role="img" aria-label="Orange supplement jar"></div><p class="pn">Flexa-Core™ Care<br>1500mg Glucosamine<br>x 180 tablets</p><p class="stars">★★★★★</p><p class="pr">from $11.89</p><span class="add">Add to Cart</span></div>
    <div class="card boxed"><div class="jar" role="img" aria-label="Orange supplement jar"></div><p class="pn">Flexa-Core™ Care<br>1500mg Glucosamine<br>x 180 tablets</p><p class="stars">★★★★★</p><p class="pr">from $11.89</p><span class="add">Add to Cart</span></div>
    <div class="card boxed"><div class="jar" role="img" aria-label="Orange supplement jar"></div><p class="pn">Flexa-Core™ Care<br>1500mg Glucosamine<br>x 180 tablets</p><p class="stars">★★★★★</p><p class="pr">from $11.89</p><span class="add">Add to Cart</span></div>
    <div class="card boxed"><div class="jar" role="img" aria-label="Orange supplement jar"></div><p class="pn">Flexa-Core™ Care<br>1500mg Glucosamine<br>x 180 tablets</p><p class="stars">★★★★★</p><p class="pr">from $11.89</p><span class="add">Add to Cart</span></div>
    <div class="card boxed"><div class="jar" role="img" aria-label="Orange supplement jar"></div><p class="pn">Flexa-Core™ Care<br>1500mg Glucosamine<br>x 180 tablets</p><p class="stars">★★★★★</p><p class="pr">from $11.89</p><span class="add">Add to Cart</span></div>
    <div class="card boxed"><div class="jar" role="img" aria-label="Orange supplement jar"></div><p class="pn">Flexa-Core™ Care<br>1500mg Glucosamine<br>x 180 tablets</p><p class="stars">★★★★★</p><p class="pr">from $11.89</p><span class="add">Add to Cart</span></div>
  </div>
  <div class="more" style="left:171px;top:972px;width:524px">See More</div>
  <div class="msg" style="left:656px;top:973px;width:94px;height:18px">Send us a message</div>
  <footer class="foot" style="top:1000px;height:265px">
    <div class="col c1"><h5>Help &amp; Information</h5><p>About Us<br>Careers at Brindle<br>Corporate Responsibility<br>Investors Site</p></div>
    <div class="col c2"><h5>About Solvia</h5><p>About Us<br>Careers at Brindle<br>Corporate Responsibility<br>Investors Site</p></div>
    <div class="col c3"><h5>More From Solvia</h5><p>About Us<br>Careers at Brindle<br>Corporate Responsibility<br>Investors Site</p></div>
    <div class="col c4"><h5>Our &nbsp;Partners</h5><p>About Us<br>Careers at Brindle<br>Corporate Responsibility<br>Investors Site</p></div>
  </footer>
</section>

<!-- ===== Account: log in & sign up ===== -->
<section class="screen auth">
  <div class="box" style="left:80px;top:40px;width:221px;height:340px">
    <p class="t welcome" style="top:12px">Welcome!</p>
    <p class="t head" style="top:34px">Log In</p>
    <p class="t lbl" style="top:70px">Email</p>
    <span class="inp" style="left:14px;top:93px;width:192px"></span>
    <p class="t lbl" style="top:121px">Password</p>
    <span class="inp" style="left:14px;top:144px;width:192px"></span>
    <p class="t small" style="top:173px">Forgot Password</p>
    <span class="pill" style="left:57px;top:194px;width:106px">Log In</span>
    <div class="abs" style="left:14px;top:226px;width:192px;border-top:1px solid #999"></div>
    <span class="abs small" style="left:102px;top:220px;background:#fff;padding:0 4px">OR</span>
    <p class="t small" style="top:235px">Login With</p>
    <div class="social">
      <span><i></i>Pixogram</span><span><i></i>snoople</span><span><i></i>pagebook</span><span><i></i>chirpnet</span>
    </div>
    <p class="t small" style="top:300px">New to Solvia?</p>
    <p class="t small" style="top:318px;font-size:7px">Create Account</p>
  </div>

  <div class="box" style="left:35px;top:450px;width:310px;height:455px">
    <p class="t welcome" style="left:18px;top:14px">Welcome!</p>
    <p class="t head" style="left:18px;top:36px">Sign Up</p>
    <p class="t lbl" style="left:18px;top:72px">Name</p>
    <span class="inp" style="left:18px;top:95px;width:275px"></span>
    <p class="t lbl" style="left:18px;top:123px">Email</p>
    <span class="inp" style="left:18px;top:146px;width:275px"></span>
    <p class="t lbl" style="left:18px;top:174px">Password</p>
    <span class="inp" style="left:18px;top:197px;width:275px"></span>
    <p class="t lbl" style="left:18px;top:226px">Repeat Password</p>
    <span class="inp" style="left:18px;top:248px;width:275px"></span>
    <p class="t lbl" style="left:18px;top:277px">Gender</p>
    <span class="inp" style="left:18px;top:300px;width:84px"></span>
    <p class="t lbl" style="left:18px;top:328px">Date of Birth</p>
    <span class="inp" style="left:18px;top:351px;width:84px"></span>
    <span class="abs" style="left:18px;top:391px;width:10px;height:10px;border:1px solid #888"></span>
    <p class="t lbl" style="left:37px;top:388px;font-size:10px">I agree to the Terms &amp; Conditions</p>
    <span class="pill" style="left:102px;top:421px;width:107px">Register</span>
  </div>
</section>

<!-- ===== Product detail ===== -->
<section class="screen" style="left:0;top:1332px;width:785px;height:550px">
  <header class="hdr">
    <div class="brand"><b>Solvia</b><span>RESTORE &nbsp;|&nbsp; RENEW &nbsp;|&nbsp; THRIVE</span></div>
    <div class="search"><span>Search</span><i></i></div>
    <span class="hlink login">Log In</span><span class="hlink signup">Sign Up</span>
    <span class="cart"><svg width="18" height="14" viewBox="0 0 18 14"><path d="M0 1h3l2 8h9l2-6H4" fill="none" stroke="#111" stroke-width="1.3"/><circle cx="6.5" cy="12" r="1.3"/><circle cx="12.5" cy="12" r="1.3"/></svg><em>0</em></span>
  </header>
  <nav class="nav"><span>VITAMINS</span><span>NOOTROPICS</span><span>ABOUT US</span><span>CONTACT US</span></nav>
  <p class="ptitle">Product</p>
  <div class="hr" style="top:108px"></div>
  <div class="hr" style="top:306px"></div>
  <div class="vr" style="left:332px"></div>
  <div class="vr" style="left:453px"></div>
  <div class="abs spec">
    <p>Name:</p><b>Flexa-Core™ Care<br>1500mg Glucosamine<br>x 180 tablets</b>
    <p>Dosage:</p><b>1500mg Glucosamine<br>x 180 tablets</b>
    <p>Review:</p><b>5 Star<br>145 Reviews</b>
  </div>
  <div class="abs bigjar" role="img" aria-label="Orange supplement jar"></div>
  <div class="abs buy">
    <h2>Flexa-Core™ Care 1500mg<br>Glucosamine x 180<br>tablets</h2>
    <p class="big-stars">★★★★★</p>
    <p class="line"><span>Price:</span><strong>$11.89</strong></p>
    <p class="line"><span>Amount:</span><strong>- 1 +</strong></p>
    <span class="pill">Add to Cart</span>
  </div>
  <h3 class="abs desc-h" style="font-weight:400">Description</h3>
  <div class="dcol" style="left:57px;width:250px">
    <p>Flexa-Core™ Care 1500mg Glucosamine x 180 tablets</p>
    <p>Acai Berry 4000mg tablets contain 800mg of 5:1 Acai extract (equivalent of 4000mg Acai berry) along with 200mg of Garcinia Cambogia, Chromium polynicotinate and gymnema sylvestre extract.</p>
    <p>Value for money:</p>
    <p>Acai Berry 4000mg is sold in bottles containing 3 months supply and with prices starting at just £4.16 a month, they offer great value for money.</p>
  </div>
  <div class="dcol" style="left:313px;width:160px">
    <p>Why buy from us:</p>
    <p>We pride ourselves on giving you the best quality products for optimum results and maximum value. We make no ridiculous claims and we do not sell over hyped products.</p>
    <p>Directions:</p>
    <p>Take one tablet daily, preferably with a meal. Do not exceed stated dose.</p>
  </div>
  <div class="dcol" style="left:479px;width:245px">
    <p>Ingredients:</p>
    <p>Serving Size: 1 tablet<br>Servings Per Container: 180<br>Acai Berry Extract 5:1(Providing equivalent of 4000mg Acai Berry): 800mg<br>Proprietary Blend of Garcinia cambogia extract, Chromium Polynicotinate, Gymnema sylvestre extract: 800mg<br>Other ingredients: Microcrystalline Cellulose, Magnesium Stearate, Dicalcium Phosphate, Coating (Hypromellose, Glycerin)</p>
  </div>
  <footer class="foot" style="top:468px;height:82px">
    <div class="col c1"><h5>Help &amp; Information</h5><p>About Us<br>Careers at Brindle<br>Corporate Responsibility<br>Investors Site</p></div>
    <div class="col c2"><h5>About Solvia</h5><p>About Us<br>Careers at Brindle<br>Corporate Responsibility<br>Investors Site</p></div>
    <div class="col c3"><h5>More From Solvia</h5><p>About Us<br>Careers at Brindle<br>Corporate Responsibility<br>Investors Site</p></div>
    <div class="col c4"><h5>Our &nbsp;Partners</h5><p>About Us<br>Careers at Brindle<br>Corporate Responsibility<br>Investors Site</p></div>
  </footer>
</section>

<!-- ===== Shopping cart ===== -->
<section class="screen" style="left:805px;top:1290px;width:750px;height:420px">
  <header class="hdr">
    <div class="brand"><b>Solvia</b><span>RESTORE &nbsp;|&nbsp; RENEW &nbsp;|&nbsp; THRIVE</span></div>
    <div class="search"><span>Search</span><i></i></div>
    <span class="hlink login">Log In</span><span class="hlink signup">Sign Up</span>
    <span class="cart"><svg width="18" height="14" viewBox="0 0 18 14"><path d="M0 1h3l2 8h9l2-6H4" fill="none" stroke="#111" stroke-width="1.3"/><circle cx="6.5" cy="12" r="1.3"/><circle cx="12.5" cy="12" r="1.3"/></svg><em>0</em></span>
  </header>
  <nav class="nav"><span>VITAMINS</span><span>NOOTROPICS</span><span>ABOUT US</span><span>CONTACT US</span></nav>
  <p class="abs cart-title">Shopping Cart</p>
  <div class="hr" style="top:98px"></div>
  <table class="items">
    <tr><th></th><th>Product Name</th><th>Qty</th><th>Unit Price</th></tr>
    <tr><td class="x">X</td><td>Flexa-Core™ Care 1500mg Glucosamine x 180 tablets</td><td class="q">1</td><td class="p">$11.89</td></tr>
    <tr><td class="x">X</td><td>Flexa-Core™ Care 1500mg Glucosamine x 180 tablets</td><td class="q">1</td><td class="p">$11.89</td></tr>
    <tr><td class="x">X</td><td>Flexa-Core™ Care 1500mg Glucosamine x 180 tablets</td><td class="q">1</td><td class="p">$11.89</td></tr>
    <tr><td class="x">X</td><td>Flexa-Core™ Care 1500mg Glucosamine x 180 tablets</td><td class="q">1</td><td class="p">$11.89</td></tr>
  </table>
  <table class="totals">
    <tr><th colspan="2">Cart Totals</th></tr>
    <tr><td>Sub Totals</td><td class="v">$47.56</td></tr>
    <tr><td>Grand Totals</td><td class="v">$47.56</td></tr>
  </table>
  <span class="pill cbtn" style="left:53px">Continue Shopping</span>
  <span class="pill cbtn" style="left:333px">Modify Cart</span>
  <span class="pill cbtn" style="left:595px">Checkout</span>
  <footer class="foot" style="top:338px;height:82px">
    <div class="col c1"><h5>Help &amp; Information</h5><p>About Us<br>Careers at Brindle<br>Corporate Responsibility<br>Investors Site</p></div>
    <div class="col c2"><h5>About Solvia</h5><p>About Us<br>Careers at Brindle<br>Corporate Responsibility<br>Investors Site</p></div>
    <div class="col c3"><h5>More From Solvia</h5><p>About Us<br>Careers at Brindle<br>Corporate Responsibility<br>Investors Site</p></div>
    <div class="col c4"><h5>Our &nbsp;Partners</h5><p>About Us<br>Careers at Brindle<br>Corporate Responsibility<br>Investors Site</p></div>
  </footer>
</section>

</div>
</body>
</html>
```